Outdoor sign for Brindle Auto Restoration

I need a horizontal 4'x 8' outdoor roadside sign for my classic auto restoration business. I have uploaded colors and our logo. Needs the Brindle name, a prominent Classic AUTO RESTORATION, phone number and website. We rebuild and restore vintage cars, trucks and 4x4s. I'd like something clean but possibly retro. Classic Auto Restoration is more important than the Brindle name. It needs to be visible and readable from the street. NO CLIP ART

Target Market(s)

Customers who need their vintage care restored or upgraded. Men and women ages 25-75

Industry/Entity Type

Automotive

Colors
FFC000
F8CF3A
FAE287
FDF2CF
FEFAEE

Requirements
Must have
• Legible. Bright. Readable as a backlit 4' x 8' large horizontal sign (roughly 120cm X 240cm)
Nice to have
• Use of the Brindle logo/type, Complete or Classic before prominent AUTO RESTORATION
Should not have
• Clip art of old cars or icons. And we don't want the Brindle Logo from the website because it wont be legible from the road. I have included the Illustrator file for Brindle text in the uploads

```html
<!DOCTYPE html>
<html lang="en">
<head>
<meta charset="utf-8">
<title>Brindle Auto Restoration – Roadside Sign</title>
<link rel="stylesheet" href="https://fonts.googleapis.com/css2?family=Roboto+Condensed:wght@700&display=swap">
<style>
  :root {
    --sign-black: #231f20;
    --sign-yellow: #f6a91c;
    --sign-white: #ffffff;
    --page-bg: #ffffff;
  }
  html, body {
    margin: 0;
    padding: 0;
    width: 1200px;
    height: 1198px;
    overflow: hidden;
    background: var(--page-bg);
  }
  .canvas {
    position: relative;
    width: 1200px;
    height: 1198px;
  }
  .roadside-sign {
    position: absolute;
    left: 262px;
    top: 93px;
    width: 676px;
    height: 331px;
    display: block;
  }
  .sign-text {
    font-family: "Roboto Condensed", "Arial Narrow", sans-serif;
    font-weight: 700;
  }
  .brand-name { fill: var(--sign-yellow); font-size: 76px; }
  .tagline { fill: var(--sign-black); font-size: 22px; }
  .headline { fill: var(--sign-white); font-size: 92px; }
  .phone-number { fill: var(--sign-black); font-size: 47px; }
  .website { fill: var(--sign-yellow); font-size: 15px; letter-spacing: 6px; }
</style>
</head>
<body>
<main class="canvas">
  <svg class="roadside-sign" viewBox="0 0 676 331" xmlns="http://www.w3.org/2000/svg" role="img" aria-label="Brindle Complete Auto Restoration sign">
    <rect class="sign-panel" x="0" y="0" width="676" height="331" fill="var(--sign-black)"/>

    <text class="sign-text brand-name" x="338" y="92" text-anchor="middle" textLength="300" lengthAdjust="spacingAndGlyphs">BRINDLE</text>

    <path class="band-edge" d="M0 137 H676 V275 Q338 206 0 272 Z" fill="var(--sign-white)"/>
    <path class="headline-band" d="M0 146 H676 V266 Q338 201 0 263 Z" fill="var(--sign-yellow)"/>

    <rect class="tagline-box" x="271" y="118" width="135" height="30" fill="var(--sign-white)"/>
    <text class="sign-text tagline" x="338.5" y="141" text-anchor="middle">COMPLETE</text>

    <text class="sign-text headline" x="30" y="232" textLength="594" lengthAdjust="spacingAndGlyphs">AUTO RESTORATION</text>

    <rect class="phone-box" x="175" y="239" width="326" height="49" fill="var(--sign-white)"/>
    <g class="phone-icon" transform="translate(201 263)">
      <circle r="17" fill="none" stroke="var(--sign-black)" stroke-width="4"/>
      <path d="M-7 -8 L-3 -9 L0 -3 L-2 -1 Q0 3 3 5 L5 3 L10 6 L9 10 Q6 12 2 10 Q-6 6 -9 -2 Q-10 -6 -7 -8 Z" fill="var(--sign-black)"/>
    </g>
    <text class="sign-text phone-number" x="223" y="281" textLength="273" lengthAdjust="spacingAndGlyphs">501-555-0147</text>

    <text class="sign-text website" x="340" y="315" text-anchor="middle">www.brindleautoworks.com</text>
  </svg>
</main>
</body>
</html>
```